Bespoke Builders Business Card Design

We need a business card for an established builder of high quality bespoke homes in Auckland and Northland. We build and renovate homes collaboratively facilitating effective communication between owners, builders, architects, suppliers and tradespeople. We have never built or renovated a home that leaks or has faults. We only use reliable materials. We have never been sued or had legal action taken against us. We are honest builders of bespoke homes not group mass produced homes. Our niche market is in character homes. We practice sustainability and have built a lot of coastal property. We have been in business for over thirty years . We would like to see natural colors of the environment sand,sea and maybe vegetation . The design should communicate quality, sustainability,fair pricing, open communication and the originality of bespoke building. And the fact that the builder is registered.

Business

Rowan Tillery Builders
Ph. 027318592
18 Garnet Rd Ferndale Bay Auckland 0814
PO Box 958 Mangawhai 0371

```html
<!DOCTYPE html>
<html lang="en">
<head>
<meta charset="utf-8">
<title>Rowan Tillery Builders – Business Card</title>
<link rel="stylesheet" href="https://fonts.googleapis.com/css2?family=Didact+Gothic&display=swap">
<style>
  :root {
    --backdrop: #e9e4dc;
    --kraft: #c6a47b;
    --kraft-edge: #b8956b;
    --ink: #4b4a48;
  }
  * { margin: 0; padding: 0; box-sizing: border-box; }
  html, body {
    width: 1200px;
    height: 851px;
    overflow: hidden;
    background: var(--backdrop);
    font-family: "Didact Gothic", "Century Gothic", sans-serif;
    color: var(--ink);
  }
  .sheet {
    position: relative;
    width: 1200px;
    height: 851px;
  }
  .card {
    position: absolute;
    top: 268px;
    width: 525px;
    height: 315px;
    background: var(--kraft);
    border: 1px solid var(--kraft-edge);
    box-shadow: 0 6px 18px rgba(60, 40, 20, 0.18);
  }
  .card--front { left: 50px; }
  .card--back  { left: 625px; }

  .wordmark {
    position: absolute;
    left: 118px;
    top: 108px;
    display: flex;
    align-items: center;
    gap: 14px;
  }
  .wordmark__square {
    width: 44px;
    height: 44px;
    background: var(--ink);
  }
  .wordmark__text {
    display: flex;
    flex-direction: column;
    line-height: 1;
  }
  .wordmark__name {
    font-size: 34px;
    letter-spacing: 0.5px;
  }
  .wordmark__trade {
    align-self: flex-end;
    margin-top: 4px;
    font-size: 17px;
    letter-spacing: 3.5px;
  }

  .card--back .wordmark {
    left: auto;
    right: 34px;
    top: 34px;
    transform: scale(0.8);
    transform-origin: right top;
  }

  .contact {
    position: absolute;
    left: 34px;
    bottom: 30px;
    list-style: none;
    font-size: 16px;
    line-height: 1.65;
  }
  .contact__item {
    display: flex;
    align-items: center;
    gap: 10px;
  }
  .contact__icon {
    width: 14px;
    height: 14px;
    fill: var(--ink);
    flex: none;
  }
</style>
</head>
<body>
<main class="sheet">
  <section class="card card--front" aria-label="Card front">
    <div class="wordmark">
      <span class="wordmark__square"></span>
      <div class="wordmark__text">
        <span class="wordmark__name">Rowan Tillery</span>
        <span class="wordmark__trade">BUILDERS</span>
      </div>
    </div>
  </section>

  <section class="card card--back" aria-label="Card back">
    <div class="wordmark">
      <span class="wordmark__square"></span>
      <div class="wordmark__text">
        <span class="wordmark__name">Rowan Tillery</span>
        <span class="wordmark__trade">BUILDERS</span>
      </div>
    </div>
    <ul class="contact">
      <li class="contact__item">
        <svg class="contact__icon" viewBox="0 0 16 16" aria-hidden="true">
          <path d="M1 5c0-2 3-3 7-3s7 1 7 3v1h-4V4.5H5V6H1z"/>
          <rect x="3" y="7" width="10" height="7" rx="1"/>
        </svg>
        <span>027318592</span>
      </li>
      <li class="contact__item">
        <svg class="contact__icon" viewBox="0 0 16 16" aria-hidden="true">
          <path d="M8 1a5 5 0 0 0-5 5c0 4 5 9 5 9s5-5 5-9a5 5 0 0 0-5-5zm0 7a2 2 0 1 1 0-4 2 2 0 0 1 0 4z"/>
        </svg>
        <span>18 Garnet Rd Ferndale Bay Auckland 0814</span>
      </li>
      <li class="contact__item">
        <svg class="contact__icon" viewBox="0 0 16 16" aria-hidden="true">
          <path d="M8 1a5 5 0 0 0-5 5c0 4 5 9 5 9s5-5 5-9a5 5 0 0 0-5-5zm0 7a2 2 0 1 1 0-4 2 2 0 0 1 0 4z"/>
        </svg>
        <span>PO Box 958 Mangawhai 0371</span>
      </li>
    </ul>
  </section>
</main>
</body>
</html>
```